依頼概要
■依頼の目的/概要
大型施設の共有スペースに展示する商品のPOPのデザインをお願いします。
展示の全体イメージがありますのでそれに合わせたイメージで制作して下さい。

■依頼詳細
大型SC内の新店舗の商品展示用のPOPになります。
展示イメージに合うようにPOPの制作をして下さい。
前回の展示のPOPを参考にアップしておきますが、同じような配置にする必要はございません。
前回は背景色などは変えずに、商品名、金額等を、レディース、メンズ、キッズの三種類に色分けして区別しておりました。
今回はキッズはないのですが、レディース、メンズ、雑貨と別れておりますので、うまく区別できるような工夫をお願いします。
サイズは A4縦サイズ。
店舗によって商品、金額、アイテム数は変化するので、変更できるような仕様にして下さい。
フォントはモリサワでしたら入っております。
採用後は使用フォントを納品データと共にお知らせください。

■重視する点
Illustrator・Photoshopの経験必須でお願いします。
新店舗のPOPになりますので、」お客様の目に留まるようなデザインが望ましいです。

■継続依頼について
弊社ではこういった案件が多くあり、次回は母の日、父の日等もありますので、継続的依頼できるありがたいです。

その他何かご不明な点がございましたら、お気軽にご質問下さい。
よろしくお願いいたします。
参考用イメージをアップします。

今回の展示イメージ
前回のPOPイメージ

の2点です。
1店舗の最大アイテム数は6になります。
前回のPOP参考例はあくまで参考です。
同じように作作らなくても良いので参考程度にして頂ければ幸いです。
展示イメージにある通り、POPは各マネキン、雑貨の前に置くものになります。
新店舗のオープンなのでワクワクするようなイメージで制作してもらえればと思います。
集まりが少ないので当選額を上乗せします。
それに伴い期間も延長いたします。
ご応募いただきありがとうございました。

見やすくイメージに沿っていたため。

たくさんのご参加ありがとうございました。
ぜひ次回もご参加下さい。

```html
<!DOCTYPE html>
<html lang="ja">
<head>
<meta charset="utf-8">
<title>メンズ商品POP</title>
<link rel="stylesheet" href="https://fonts.googleapis.com/css2?family=M+PLUS+1p:wght@800;900&family=Noto+Sans+JP:wght@500;700;900&family=Noto+Serif+JP:wght@700;900&display=swap">
<style>
  :root{
    --title-purple:#5a2a8c;
    --item-blue:#1f4fb8;
    --price-blue:#2a4a9a;
    --bg-pale:#dbe7f5;
    --stripe:#c6d9ef;
    --banner-white:#ffffff;
    --banner-edge:#b9cbe3;
    --shop-bar-top:#8fb4e6;
    --shop-bar-bottom:#3f74c6;
    --ink:#333a46;
  }
  *{margin:0;padding:0;box-sizing:border-box}
  html,body{width:846px;height:1200px;overflow:hidden;background:#fff}
  .pop{
    position:relative;width:846px;height:1200px;overflow:hidden;
    background:repeating-linear-gradient(90deg,var(--bg-pale) 0 28px,var(--stripe) 28px 56px);
    font-family:"Noto Sans JP",sans-serif;color:var(--ink);
  }
  .store-photo{
    position:absolute;left:0;top:0;width:846px;height:255px;
    background:linear-gradient(180deg,#9fb1c8 0%,#c9d6e6 55%,#e6edf6 100%);
  }
  .title{
    position:absolute;left:0;right:0;top:6px;text-align:center;
    font-family:"M PLUS 1p",sans-serif;font-weight:900;font-size:116px;letter-spacing:4px;
    color:var(--title-purple);
    text-shadow:0 0 6px #fff,0 0 6px #fff,3px 3px 0 #fff,-3px -3px 0 #fff,3px -3px 0 #fff,-3px 3px 0 #fff;
  }
  .appeal{
    position:absolute;right:18px;top:196px;font-size:30px;font-weight:700;color:#222;
  }
  .category-tag{
    position:absolute;left:56px;top:212px;width:128px;height:44px;border-radius:22px;
    background:#fff;border:2px solid #7d9fd0;
    display:flex;align-items:center;justify-content:center;
    font-weight:900;font-size:24px;color:var(--item-blue);
  }
  .items{position:absolute;left:70px;top:268px;width:736px;list-style:none}
  .item{
    position:relative;height:104px;margin-bottom:28px;
    background:linear-gradient(180deg,#fff 0%,#f3f7fc 100%);
    border:2px solid var(--banner-edge);
    box-shadow:3px 4px 6px rgba(60,90,140,.25);
  }
  .item-ornament{
    position:absolute;top:8px;width:100px;height:86px;border-radius:8px;
    background:linear-gradient(135deg,#e3ebf7,#c9d7ee);
  }
  .item-ornament.left{left:8px}
  .item-ornament.right{right:8px;width:92px;border-radius:50%}
  .item-name{
    position:absolute;left:124px;top:21px;line-height:1;white-space:nowrap;
    font-weight:900;font-size:58px;color:var(--item-blue);
  }
  .item-price{
    position:absolute;left:436px;top:10px;line-height:1;white-space:nowrap;
    font-family:"Noto Serif JP",serif;font-weight:900;font-size:46px;color:var(--price-blue);
  }
  .item-tax{
    position:absolute;left:442px;top:64px;line-height:1;white-space:nowrap;
    font-family:"Noto Serif JP",serif;font-weight:700;font-size:20px;color:var(--ink);
  }
  .shop-logo{
    position:absolute;left:14px;top:1044px;width:198px;height:141px;
    background:#eef3fa;border:2px solid #5b6b80;
  }
  .shop-logo svg{position:absolute;inset:0}
  .shop-logo span{
    position:absolute;left:0;right:0;bottom:24px;text-align:center;font-size:24px;color:#333;
  }
  .shop-bar{
    position:absolute;left:226px;top:1066px;width:606px;height:84px;border-radius:42px;
    background:linear-gradient(180deg,var(--shop-bar-top),var(--shop-bar-bottom));
    border:2px solid #2f5da6;
  }
  .shop-name{
    position:absolute;left:190px;top:14px;font-size:40px;font-weight:700;color:#fff;
  }
  .floor{
    position:absolute;left:354px;top:13px;width:54px;height:54px;border-radius:50%;
    background:#fff;border:2px solid #2f5da6;color:var(--item-blue);
    display:flex;align-items:center;justify-content:center;font-size:24px;font-weight:700;
  }
  .corporate-logo{
    position:absolute;right:18px;top:1160px;font-size:20px;color:#444;
  }
</style>
</head>
<body>
<div class="pop">
  <div class="store-photo" role="img" aria-label="明るい店内の衣料品売り場の写真"></div>
  <h1 class="title">タイトル</h1>
  <p class="appeal">アピールコメント</p>
  <p class="category-tag">メンズ</p>

  <ul class="items">
    <li class="item"><div class="item-ornament left" role="img" aria-label="飾り模様"></div><span class="item-name">ジャケット</span><span class="item-price">¥5,900</span><span class="item-tax">税込¥6,372</span><div class="item-ornament right" role="img" aria-label="花の飾り"></div></li>
    <li class="item"><div class="item-ornament left" role="img" aria-label="飾り模様"></div><span class="item-name">ジャケット</span><span class="item-price">¥5,900</span><span class="item-tax">税込¥6,372</span><div class="item-ornament right" role="img" aria-label="花の飾り"></div></li>
    <li class="item"><div class="item-ornament left" role="img" aria-label="飾り模様"></div><span class="item-name">ジャケット</span><span class="item-price">¥5,900</span><span class="item-tax">税込¥6,372</span><div class="item-ornament right" role="img" aria-label="花の飾り"></div></li>
    <li class="item"><div class="item-ornament left" role="img" aria-label="飾り模様"></div><span class="item-name">ジャケット</span><span class="item-price">¥5,900</span><span class="item-tax">税込¥6,372</span><div class="item-ornament right" role="img" aria-label="花の飾り"></div></li>
    <li class="item"><div class="item-ornament left" role="img" aria-label="飾り模様"></div><span class="item-name">ジャケット</span><span class="item-price">¥5,900</span><span class="item-tax">税込¥6,372</span><div class="item-ornament right" role="img" aria-label="花の飾り"></div></li>
    <li class="item"><div class="item-ornament left" role="img" aria-label="飾り模様"></div><span class="item-name">ジャケット</span><span class="item-price">¥5,900</span><span class="item-tax">税込¥6,372</span><div class="item-ornament right" role="img" aria-label="花の飾り"></div></li>
  </ul>

  <div class="shop-logo">
    <svg width="198" height="141" viewBox="0 0 198 141"><line x1="0" y1="0" x2="198" y2="141" stroke="#5b6b80" stroke-width="2"/></svg>
    <span>店舗ロゴ</span>
  </div>
  <div class="shop-bar">
    <span class="shop-name">店舗名</span>
    <span class="floor">2階</span>
  </div>
  <p class="corporate-logo">コーポレートロゴ</p>
</div>
</body>
</html>
```